Business card

Hi Marta,
can you please design business cards for me?
Based on your Brimvale design please go crazy (still retain a professional business-solid profile). I would like to use really stylish paper (or different paper types and special prints like partly embossed or partly glossy and contrast the glossiness with matt for instance).
Please keep in mind that I might come back to you in several months if the business requires other print material like stationary, folders, envelopes etc. It all needs to be in line and make a huge impression without going over board and still remain very solid and serious.
I know that's a lot to ask and I apologise but I am really impressed with your work so far and have no doubt that you can spin the wheels again in a great way.
Thanks bunches, Lukas
In order to punch in the right text from the outset, here is some key data:
Brimvale
Your next level
Lukas Brander
Chief Executive Growth Partner
+41 79 583 1067
lukas.brander@brimvale.com
brimvale.com
Business
Brimvale
Your next level
Lukas Brander
+41 79 583 1067
brimvale.com

```html
<!DOCTYPE html>
<html lang="en">
<head>
<meta charset="utf-8">
<title>Brimvale business card – Lukas Brander</title>
<link rel="stylesheet" href="https://fonts.googleapis.com/css2?family=Lato:wght@300;400;700&display=swap">
<style>
  :root {
    --backdrop: #e9e6e1;
    --card-black: #141414;
    --card-deep: #080808;
    --card-lift: #262626;
    --panel-dark: #0b0b0b;
    --panel-edge: #2a2a2a;
    --text-silver: #c9c9c9;
    --text-muted: #9a9a9a;
    --icon-grey: #8a8a8a;
    --accent-red: #c8202a;
  }
  html, body {
    margin: 0;
    padding: 0;
    width: 1200px;
    height: 800px;
    overflow: hidden;
    background: var(--backdrop);
    font-family: "Lato", "Helvetica Neue", Arial, sans-serif;
  }
  .canvas {
    position: relative;
    width: 1200px;
    height: 800px;
    display: flex;
    align-items: center;
    justify-content: center;
    gap: 40px;
  }
  .card {
    position: relative;
    width: 540px;
    height: 310px;
    background: radial-gradient(ellipse at 40% 50%, var(--card-lift) 0%, var(--card-black) 55%, var(--card-deep) 100%);
    box-shadow: 0 10px 30px rgba(0, 0, 0, 0.25);
    overflow: hidden;
    color: var(--text-silver);
  }
  .card-fold {
    position: absolute;
    inset: 0;
    width: 540px;
    height: 310px;
    pointer-events: none;
  }
  .fold-panel { fill: var(--panel-dark); opacity: 0.75; }
  .fold-edge { fill: url(#fold-sheen); }
  .fold-edge-back { fill: url(#fold-sheen-back); }

  /* front: identity block */
  .identity {
    position: absolute;
    top: 62px;
    left: 370px;
    width: 160px;
  }
  .identity-name {
    margin: 0;
    font-size: 17px;
    font-weight: 700;
    letter-spacing: 1.5px;
    text-transform: uppercase;
    color: var(--text-silver);
    white-space: nowrap;
  }
  .identity-rule {
    height: 2px;
    width: 150px;
    margin: 5px 0 6px;
    background: var(--accent-red);
  }
  .identity-role {
    margin: 0;
    font-size: 7.5px;
    letter-spacing: 0.6px;
    text-transform: uppercase;
    color: var(--text-muted);
    white-space: nowrap;
  }

  /* front: contact lines */
  .contact-list {
    position: absolute;
    top: 122px;
    right: 226px;
    margin: 0;
    padding: 0;
    list-style: none;
    text-align: right;
  }
  .contact-item {
    display: flex;
    align-items: center;
    justify-content: flex-end;
    gap: 8px;
    font-size: 15px;
    font-weight: 300;
    line-height: 22px;
    letter-spacing: 0.3px;
    color: var(--text-silver);
    white-space: nowrap;
  }
  .contact-icon {
    width: 13px;
    height: 13px;
    flex: none;
  }

  /* back: brand mark and web address */
  .brand-mark {
    position: absolute;
    top: 58px;
    right: 42px;
    display: flex;
    align-items: center;
    gap: 7px;
    font-size: 17px;
    font-weight: 700;
    color: var(--text-silver);
  }
  .brand-dot {
    width: 9px;
    height: 9px;
    border-radius: 50%;
    background: var(--accent-red);
  }
  .web-block {
    position: absolute;
    top: 150px;
    left: 56px;
    text-align: right;
  }
  .web-address {
    margin: 0;
    font-size: 30px;
    font-weight: 300;
    letter-spacing: 0.2px;
    color: var(--text-silver);
    white-space: nowrap;
  }
  .web-tagline {
    margin: 2px 0 0;
    font-size: 9px;
    letter-spacing: 0.6px;
    text-transform: uppercase;
    color: var(--text-muted);
    white-space: nowrap;
  }
</style>
</head>
<body>
<main class="canvas">

  <section class="card card--front" aria-label="Business card front">
    <svg class="card-fold" viewBox="0 0 540 310" aria-hidden="true">
      <defs>
        <linearGradient id="fold-sheen" x1="0" y1="0" x2="1" y2="0">
          <stop offset="0" stop-color="#000" stop-opacity="0.7"/>
          <stop offset="0.35" stop-color="#2a2a2a" stop-opacity="0.45"/>
          <stop offset="1" stop-color="#2a2a2a" stop-opacity="0"/>
        </linearGradient>
      </defs>
      <polygon class="fold-panel" points="362,0 540,0 540,310 300,310"/>
      <polygon class="fold-edge" points="362,0 410,0 348,310 300,310"/>
    </svg>

    <div class="identity">
      <h1 class="identity-name">Lukas Brander</h1>
      <div class="identity-rule"></div>
      <p class="identity-role">Chief Executive Growth Partner</p>
    </div>

    <ul class="contact-list">
      <li class="contact-item">+41 79 583 1067
        <svg class="contact-icon" viewBox="0 0 16 16" aria-hidden="true">
          <path d="M2 5c0-2 1-3 6-3s6 1 6 3v1h-3V5H5v1H2z" fill="#8a8a8a"/>
          <rect x="3" y="7" width="10" height="7" rx="1.5" fill="#8a8a8a"/>
          <circle cx="8" cy="10.5" r="1.8" fill="#1a1a1a"/>
        </svg>
      </li>
      <li class="contact-item">www.brimvale.com
        <svg class="contact-icon" viewBox="0 0 16 16" aria-hidden="true">
          <rect x="1" y="2" width="14" height="10" rx="1" fill="#8a8a8a"/>
          <rect x="2.5" y="3.5" width="11" height="7" fill="#1a1a1a"/>
          <rect x="6" y="12" width="4" height="2" fill="#8a8a8a"/>
        </svg>
      </li>
      <li class="contact-item">lukas.brander@brimvale.com
        <svg class="contact-icon" viewBox="0 0 16 16" aria-hidden="true">
          <rect x="1.5" y="3" width="13" height="10" fill="none" stroke="#8a8a8a" stroke-width="1.3"/>
          <path d="M1.5 3l6.5 5.5L14.5 3" fill="none" stroke="#8a8a8a" stroke-width="1.3"/>
        </svg>
      </li>
    </ul>
  </section>

  <section class="card card--back" aria-label="Business card back">
    <svg class="card-fold" viewBox="0 0 540 310" aria-hidden="true">
      <defs>
        <linearGradient id="fold-sheen-back" x1="0" y1="0" x2="1" y2="0">
          <stop offset="0" stop-color="#000" stop-opacity="0.7"/>
          <stop offset="0.35" stop-color="#2a2a2a" stop-opacity="0.45"/>
          <stop offset="1" stop-color="#2a2a2a" stop-opacity="0"/>
        </linearGradient>
      </defs>
      <polygon class="fold-panel" points="395,0 540,0 540,310 300,310"/>
      <polygon class="fold-edge-back" points="395,0 450,0 355,310 300,310"/>
    </svg>

    <div class="brand-mark">
      <span class="brand-dot"></span>
      <span class="brand-name">Brimvale</span>
    </div>

    <div class="web-block">
      <p class="web-address">www.brimvale.com</p>
      <p class="web-tagline">Chief Executive Growth Partner</p>
    </div>
  </section>

</main>
</body>
</html>
```